Ad Creatives for linkedin ads, google ads and facebook ads in different formats

Please provide several banner ads for linkedin, google and facebook to visualise our product offerings from our product page: https://mendoworks.com/home/tarnline-products/
Just use the product names without taking any further description into account. It should be easy to consume an give a high level overview.
Please have our attached styleguide in mind.
The formats should be:
______________
LinkedIn
- Vertical (1:1.91), square (1:1), horizontal (1.91:1)
__________
Google Ads
- Responsive Display Ads, Leaderboard (728x90), Large Rectangle (336x280), Medium Rectangle (300x250), Small Square (200x200)
____________
Facebook Ads
- Image (1200x628), Carousel (1080x1080), Video (1280x720)

```html
<!DOCTYPE html>
<html lang="en">
<head>
<meta charset="UTF-8">
<title>Mendo – Digital Insurance Platform</title>
<link rel="stylesheet" href="https://fonts.googleapis.com/css2?family=Archivo:wdth,wght@62..125,300..900&display=swap">
<style>
  :root {
    --navy-deep: #0b1430;
    --navy: #1a2645;
    --slate: #4a5878;
    --white: #ffffff;
    --orange: #f7941d;
    --orange-band: #f59e21;
    --magenta: #a01e62;
    --green: #8ab537;
  }
  html, body {
    margin: 0;
    padding: 0;
    width: 1200px;
    height: 1200px;
    overflow: hidden;
    background: var(--navy-deep);
  }
  .ad {
    position: relative;
    width: 1200px;
    height: 1200px;
    overflow: hidden;
    font-family: "Archivo", "Helvetica Neue", Arial, sans-serif;
    font-stretch: 125%;
    color: var(--white);
  }
  .hero-photo {
    position: absolute;
    inset: 0;
    background:
      radial-gradient(ellipse 45% 40% at 70% 20%, rgba(110,125,160,0.55), transparent 70%),
      radial-gradient(ellipse 35% 45% at 88% 60%, rgba(120,135,170,0.45), transparent 70%),
      linear-gradient(100deg, var(--navy-deep) 0%, #111c3a 40%, #2c3859 75%, var(--navy) 100%);
  }
  .brand {
    position: absolute;
    left: 118px;
    top: 136px;
    display: flex;
    align-items: center;
    gap: 22px;
  }
  .brand-dot {
    width: 60px;
    height: 60px;
    border-radius: 50%;
    background: var(--orange);
  }
  .brand-name {
    font-size: 58px;
    font-weight: 300;
    font-stretch: 100%;
    letter-spacing: 6px;
    line-height: 1;
    color: var(--white);
  }
  .headline {
    position: absolute;
    left: 94px;
    margin: 0;
    font-weight: 800;
    line-height: 1;
    letter-spacing: 0.5px;
  }
  .headline-lead { top: 356px; font-size: 64px; color: var(--white); }
  .headline-accent { top: 438px; font-size: 64px; color: var(--orange); }
  .band {
    position: absolute;
    left: 89px;
    height: 136px;
    display: flex;
    align-items: center;
  }
  .band-magenta {
    top: 533px;
    width: 725px;
    background: linear-gradient(90deg, var(--magenta) 0%, var(--magenta) 45%, rgba(160,30,98,0.35) 82%, rgba(160,30,98,0) 100%);
  }
  .band-orange {
    top: 691px;
    width: 560px;
    background: linear-gradient(90deg, var(--orange-band) 0%, var(--orange-band) 45%, rgba(245,158,33,0.4) 78%, rgba(245,158,33,0) 100%);
  }
  .band-text {
    font-size: 55px;
    font-weight: 800;
    letter-spacing: 1px;
    line-height: 1;
    white-space: nowrap;
  }
  .band-magenta .band-text { padding-left: 30px; }
  .band-orange .band-text { padding-left: 35px; }
  .cta {
    position: absolute;
    left: 81px;
    top: 941px;
    width: 629px;
    height: 132px;
    border-radius: 38px;
    background: var(--green);
    display: flex;
    align-items: center;
    padding-left: 72px;
    box-sizing: border-box;
    font-size: 44px;
    font-weight: 800;
    letter-spacing: 1.5px;
    color: var(--white);
    white-space: nowrap;
  }
</style>
</head>
<body>
  <main class="ad">
    <div class="hero-photo" role="img" aria-label="Blurred photo of a person working on a laptop with a translucent insurance interface showing a shield with a tick and award rosettes"></div>

    <div class="brand">
      <span class="brand-dot"></span>
      <span class="brand-name">MENDO</span>
    </div>

    <h1 class="headline headline-lead">THE PROVEN</h1>
    <p class="headline headline-accent">NEXT-GENERATION</p>

    <div class="band band-magenta"><span class="band-text">DIGITAL INSURANCE</span></div>
    <div class="band band-orange"><span class="band-text">PLATFORM</span></div>

    <div class="cta">GET FREE QUOTE</div>
  </main>
</body>
</html>
```